Property Report

8 page document, similar theme to our website (www.harbourandmeadows.com) and previous brochure (provided). All content provided. We want a professional looking document. We need ASAP. Thanks!

Industry/Entity Type

Property

Font styles to use
Serif
Sans Serif

Colors
ffc214
ffcf3e
fee18a
fff3d1

Requirements
Must have
• Page 1: Cover
Page 2: Content
Page 3: About Us
Page 4: Site Description
Page 5: Scheme
Page 6: Analysis
Page 7: Conclusion
Page 8: Contact Details

```html
<!DOCTYPE html>
<html lang="en">
<head>
<meta charset="utf-8">
<title>Site Report – Harbour &amp; Meadows Commercial</title>
<link rel="stylesheet" href="https://fonts.googleapis.com/css2?family=Lato:ital,wght@0,400;0,700;1,400&display=swap">
<style>
:root{
  --stage:#202020;
  --panel:#333333;
  --panel-soft:#3d3d3d;
  --yellow:#fbc21a;
  --yellow-light:#ffcf3e;
  --paper:#ffffff;
  --paper-grey:#ededed;
  --ink:#222222;
}
*{box-sizing:border-box;margin:0;padding:0}
html,body{width:1200px;height:1200px;overflow:hidden;background:var(--stage);font-family:'Lato',sans-serif;color:#fff}
.page{position:absolute;width:267px;height:345px;overflow:hidden;box-shadow:2px 3px 6px rgba(0,0,0,.6)}
.abs{position:absolute}
.photo{position:absolute}
.yellow{color:var(--yellow)}
.brand{font-weight:700;color:#fff;text-align:center;line-height:1.05}
p,li{font-size:5.2px;line-height:1.45}
ul{list-style:none}
li{position:relative;padding-left:7px;margin-bottom:3px}
li::before{content:"›";position:absolute;left:0;top:-1px;font-size:7px}

/* cover */
.cover .photo{inset:0;background:linear-gradient(135deg,#4e5a48,#6c7560 40%,#3f4a3a 70%,#5d6556)}
.cover-panel{left:16px;top:0;width:119px;height:264px;background:var(--panel)}
.cover-panel .brand{position:absolute;top:48px;width:100%;font-size:13px}
.cover-panel .brand small{display:block;font-size:6.5px;color:var(--yellow);font-weight:400;margin-top:2px}
.cover-title{position:absolute;top:183px;width:100%;text-align:center;font-size:16px;font-weight:700;color:var(--yellow)}
.cover-address{position:absolute;top:212px;width:100%;text-align:center;font-size:5.5px;line-height:1.4}
.cover-client{position:absolute;top:235px;width:100%;text-align:center;font-size:5.8px;line-height:1.4}

/* contents */
.contents .photo{left:0;top:0;width:132px;height:345px;background:linear-gradient(90deg,#f4f4f3,#e8e6e2 70%,#d9cbb5)}
.contents-panel{left:132px;top:0;width:135px;height:345px;background:var(--panel)}
.contents-panel h2{position:absolute;left:12px;top:30px;font-size:15px;color:var(--yellow);font-weight:700}
.toc{position:absolute;left:12px;top:58px;width:115px}
.toc-row{display:flex;font-size:7px;height:21.8px;font-weight:700}
.toc-row span:first-child{width:63px}
.toc-row span:nth-child(2){width:16px}

/* about */
.about .photo-city{inset:0;background:linear-gradient(160deg,#5a6a78,#7b7f78 40%,#5c5a4e 75%,#4b5a66)}
.about .photo-top{left:0;top:0;width:267px;height:127px;background:linear-gradient(180deg,#bdbdbd,#6d6d6d 60%,#2a2a2a)}
.about-box{left:11px;top:55px;width:130px;height:155px;background:var(--yellow);color:var(--ink);padding:7px 7px}
.about-box h2{font-size:13px;font-weight:700;margin-bottom:5px}
.about-box p{font-size:4.9px;text-align:justify;margin-bottom:5px}
.thumb{top:250px;width:78px;height:78px;border:2px solid #111}
.thumb-a{left:12px;background:linear-gradient(180deg,#c7d8ea,#8b8077 60%,#6d6b66)}
.thumb-b{left:96px;background:linear-gradient(180deg,#d4e3ee,#c7b9a4 55%,#7a7565)}
.thumb-c{left:176px;background:linear-gradient(180deg,#c9dbe9,#ede4d8 55%,#a89f93)}

/* site description */
.site{background:var(--panel)}
.site .sky{left:0;top:0;width:267px;height:196px;background:linear-gradient(180deg,#8fc2e8,#c9e2f4)}
.site .frame{left:16px;top:16px;width:236px;height:186px;border:1.5px solid var(--panel);background:linear-gradient(150deg,#6fa8dc,#e8e3d6 45%,#cfc6b4 80%,#9b917f)}
.site-box{left:16px;top:207px;width:236px;height:122px;background:var(--yellow);color:var(--ink);padding:7px 16px}
.site-box h2{font-size:10px;font-weight:700;margin-bottom:5px}
.site-box p{text-align:justify;margin-bottom:5px}
.site-box li::before{color:var(--ink)}

/* scheme */
.scheme .photo{inset:0;background:linear-gradient(160deg,#667058,#8b8d78 35%,#5e6a4e 65%,#7c7a6c)}
.scheme-box{left:32px;top:240px;width:235px;height:47px;background:#fff;color:var(--ink);padding:6px 8px;border-left:3px solid var(--yellow)}
.scheme-box h2{font-size:9.5px;font-weight:700;margin-bottom:4px}

/* case studies */
.cases{background:var(--paper-grey)}
.cases-head{left:16px;top:19px;color:var(--ink)}
.cases-head h2{font-size:10px;font-weight:700}
.cases-head span{font-size:7px}
.case{width:249px;height:76px;background:var(--panel)}
.case h3{position:absolute;font-size:7.5px;color:var(--yellow);font-weight:700}
.case .meta{position:absolute;font-size:4.6px;line-height:1.7;width:130px}
.case .units{color:var(--yellow);font-weight:700}
.case .pic{position:absolute;top:7px;width:96px;height:62px;border:1.5px solid #fff;background:linear-gradient(180deg,#a9c8e6,#d3dee6 40%,#7a5545 55%,#5d9a3d 70%,#4c8a32)}
.case-1{left:2px;top:55px;border-left:4px solid var(--yellow)}
.case-2{left:16px;top:142px;border-right:4px solid var(--yellow)}
.case-3{left:2px;top:229px;border-left:4px solid var(--yellow)}

/* analysis */
.analysis{background:var(--panel-soft)}
.analysis .band{left:0;top:243px;width:267px;height:102px;background:var(--yellow)}
.analysis-head{left:16px;top:16px}
.analysis-head h2{font-size:10.5px;color:var(--yellow);font-weight:700}
.analysis-head .label{font-size:5.6px;font-weight:700;margin-top:3px}
.analysis-head em{display:block;font-size:5px;margin-top:3px}
.analysis-head p{font-size:5px;margin-top:3px}
table.valuation{position:absolute;left:16px;top:78px;width:236px;height:90px;border-collapse:collapse;background:#fff;color:var(--ink);font-size:3.9px;text-align:center}
.valuation td,.valuation th{border:.6px solid #999;padding:0}
.valuation th{font-weight:700}
.analysis .photo{left:16px;top:186px;width:236px;height:139px;background:linear-gradient(180deg,#2a7fd1,#5fa0dc 45%,#9a9790 60%,#5b8a3e 85%)}

/* conclusion */
.conclusion{background:var(--paper)}
.conclusion .column{left:16px;top:0;width:124px;height:345px;background:var(--panel)}
.conclusion .photo{left:0;top:15px;width:267px;height:137px;background:linear-gradient(180deg,#9fc4e6,#c7ccc6 40%,#bfb6a6 65%,#5d9a3a 85%);border-top:2.5px solid var(--yellow);border-bottom:2.5px solid var(--yellow)}
.concl-left{left:20px;top:168px;width:115px}
.concl-left h2{font-size:10px;color:var(--yellow);font-weight:700;margin-bottom:6px}
.concl-left p{font-size:5px;margin-bottom:6px}
.concl-left h4{font-size:5px;color:var(--yellow);margin-bottom:2px}
.concl-left li{font-size:5px;margin-bottom:1px}
.concl-right{left:144px;top:186px;width:113px;color:var(--ink)}
.concl-right h4{font-size:5.2px;font-weight:700;margin-bottom:2px}
.concl-right li{font-size:5px;margin-bottom:9px}

/* contact */
.contact{background:var(--paper)}
.contact .column{left:95px;top:0;width:116px;height:290px;background:var(--panel)}
.contact .rule{left:95px;top:290px;width:116px;height:4px;background:var(--yellow)}
.contact .brand{position:absolute;left:0;top:52px;width:116px;font-size:12px}
.contact .brand small{display:block;font-size:6.5px;color:var(--yellow);font-weight:400;margin-top:2px}
.contact-details{left:18px;top:218px;font-size:5.2px;line-height:1.5}
</style>
</head>
<body>

<!-- Page 1: cover -->
<section class="page cover" style="left:161px;top:34px">
  <div class="photo" role="img" aria-label="Aerial view of suburban houses and gardens"></div>
  <div class="abs cover-panel">
    <div class="brand">Harbour &amp; Meadows<small>Commercial</small></div>
    <h1 class="cover-title">SITE REPORT</h1>
    <p class="cover-address">118 Larchfield Road, Elmbury<br>KT9 2QP</p>
    <p class="cover-client">On behalf of<br><span class="yellow">NORTON VALE GROUP LIMITED.</span></p>
  </div>
</section>

<!-- Page 2: contents -->
<section class="page contents" style="left:465px;top:34px">
  <div class="photo" role="img" aria-label="Open white door in an empty room with wooden floor"></div>
  <div class="abs contents-panel">
    <h2>Contents</h2>
    <div class="toc">
      <div class="toc-row"><span>About Us</span><span>-</span><span>03</span></div>
      <div class="toc-row"><span>Site Description</span><span>-</span><span>04</span></div>
      <div class="toc-row"><span>Scheme</span><span>-</span><span>05</span></div>
      <div class="toc-row"><span>Case Studies</span><span>-</span><span>06</span></div>
      <div class="toc-row"><span>Analysis</span><span>-</span><span>07</span></div>
      <div class="toc-row"><span>Conclusion</span><span>-</span><span>08</span></div>
      <div class="toc-row"><span>Contact Details</span><span>-</span><span>09</span></div>
    </div>
  </div>
</section>

<!-- Page 3: about -->
<section class="page about" style="left:771px;top:34px">
  <div class="photo photo-city" role="img" aria-label="Aerial view of a city with river"></div>
  <div class="photo photo-top" role="img" aria-label="Silhouetted people at a window overlooking a skyline, black and white"></div>
  <div class="abs about-box">
    <h2>About Us</h2>
    <p>Harbour &amp; Meadows Commercial specialise in the acquisition and disposal of development, investment and commercial property in London and the Home Counties. Our consultants advise on a wide range of property types and use classes and are experts in identifying ways in which property owners can maximise value.</p>
    <p>Our considerable knowledge of the property market and creative approach to delivering maximum value, has enabled us to become one of the most active development and investment consultancies in London and the South East.</p>
  </div>
  <div class="photo thumb thumb-a" role="img" aria-label="Modern residential block"></div>
  <div class="photo thumb thumb-b" role="img" aria-label="Apartment building with balconies"></div>
  <div class="photo thumb thumb-c" role="img" aria-label="Corner commercial building"></div>
</section>

<!-- Page 4: site description -->
<section class="page site" style="left:161px;top:422px">
  <div class="photo sky" role="img" aria-label="Blue sky"></div>
  <div class="photo frame" role="img" aria-label="White apartment building seen from below"></div>
  <div class="abs site-box">
    <h2>Site Description</h2>
    <p>Harbour and Meadows Commercial have been asked by Daniel Vale the representative for Norton Vale Group Limited to advise on the best disposal method to maximise value for their property.</p>
    <ul>
      <li>The existing property measures approximately 9,655 square feet internally with parking spaces.</li>
      <li>The site was granted permitted development rights in 2016 to be converted into 11 flats and 11 parking spaces but this was no implemented.</li>
    </ul>
    <p>We understand that the vendors operate their business from the premises and the property has a designated use class of B1(a) Office/E Class.</p>
  </div>
</section>

<!-- Page 5: scheme -->
<section class="page scheme" style="left:465px;top:422px">
  <div class="photo" role="img" aria-label="Aerial view of a residential housing estate"></div>
  <div class="abs scheme-box">
    <h2>Scheme</h2>
    <p>We have taken advice form Outline Architects who have reviewed the site and have come up with a scheme for 30 residential units</p>
  </div>
</section>

<!-- Page 6: case studies -->
<section class="page cases" style="left:771px;top:422px">
  <div class="abs cases-head"><h2>Case Studies</h2><span>Comparables</span></div>
  <article class="abs case case-1">
    <h3 style="left:10px;top:10px">Riverside Homes Trust</h3>
    <div class="meta" style="left:10px;top:21px">Ashdown Clinic, Mill Road, Elmbury KT9 1AB<br><br><span class="units">37 Residential Units</span><br><b>Price :</b> £4,486,970 &nbsp; <b>Per plot :</b> £121,000<br>August 2019</div>
    <div class="pic" style="left:145px" role="img" aria-label="Brick house with lawn"></div>
  </article>
  <article class="abs case case-2">
    <div class="pic" style="left:6px" role="img" aria-label="Brick house with lawn"></div>
    <h3 style="left:108px;top:8px">Private Developer</h3>
    <div class="meta" style="left:108px;top:18px">Car Sales Show Rooms And Lock Ups Adjacent To Arterial Service Station, Orchard Road, Westfield, London SW30 4LT<br><span class="units">32 Residential Units</span><br><b>Price :</b> £1,400,000 &nbsp; <b>Per plot :</b> £44,000<br>August 2019</div>
  </article>
  <article class="abs case case-3">
    <h3 style="left:10px;top:8px">Meridian Housing</h3>
    <div class="meta" style="left:10px;top:18px">Land On The South Side Of Linden Road,<br>London SW31 6HD<br><br><span class="units">74 Residential Units</span><br><b>Price :</b> £11,050,000 &nbsp; <b>Per plot :</b> £149,000<br>June 2017</div>
    <div class="pic" style="left:145px" role="img" aria-label="Brick house with lawn"></div>
  </article>
</section>

<!-- Page 7: analysis -->
<section class="page analysis" style="left:161px;top:820px">
  <div class="abs band"></div>
  <div class="abs analysis-head">
    <h2>Analysis</h2>
    <div class="label">VALUATION</div>
    <em>Consented Site Valuation Variable</em>
    <p>Please see below assumed land valuation upon delivery of planning permission.</p>
  </div>
  <table class="valuation">
    <tr><th></th><th>30</th><th>32</th><th>34</th><th>36</th><th>38</th><th>40</th><th>42</th></tr>
    <tr><td>£ 65,000</td><td>£ 1,950,000</td><td>£ 2,080,000</td><td>£ 2,210,000</td><td>£ 2,340,000</td><td>£ 2,470,000</td><td>£ 2,600,000</td><td>£ 2,730,000</td></tr>
    <tr><td>£ 75,000</td><td>£ 2,250,000</td><td>£ 2,400,000</td><td>£ 2,550,000</td><td>£ 2,700,000</td><td>£ 2,850,000</td><td>£ 3,000,000</td><td>£ 3,150,000</td></tr>
    <tr><td>£ 85,000</td><td>£ 2,550,000</td><td>£ 2,720,000</td><td>£ 2,890,000</td><td>£ 3,060,000</td><td>£ 3,230,000</td><td>£ 3,400,000</td><td>£ 3,400,000</td></tr>
    <tr><td>£ 95,000</td><td>£ 2,850,000</td><td>£ 3,040,000</td><td>£ 3,230,000</td><td>£ 3,420,000</td><td>£ 3,610,000</td><td>£ 3,800,000</td><td>£ 3,800,000</td></tr>
    <tr><td>£ 105,000</td><td>£ 3,150,000</td><td>£ 3,360,000</td><td>£ 3,570,000</td><td>£ 3,780,000</td><td>£ 3,990,000</td><td>£ 4,200,000</td><td>£ 4,200,000</td></tr>
  </table>
  <div class="photo" role="img" aria-label="Stone and timber house under blue sky with palm trees"></div>
</section>

<!-- Page 8: conclusion -->
<section class="page conclusion" style="left:465px;top:820px">
  <div class="abs column"></div>
  <div class="photo" role="img" aria-label="Two-storey house with deck and green lawn"></div>
  <div class="abs concl-left">
    <h2>Conclusion</h2>
    <p>Package Led Land Sale Involves selling the site to a Housing Association with a contractor already in place.</p>
    <h4>Benefits:</h4>
    <ul>
      <li>Housing Association has build cost certainty.</li>
      <li>No need to tender build.</li>
      <li>More interest from HA if builder in place.</li>
      <li>HA responds better to contractor.</li>
      <li>Contractor will identify potential issues coming from HA.</li>
      <li>No SDLT or CIL.</li>
    </ul>
  </div>
  <div class="abs concl-right">
    <h4>Private Sale</h4>
    <ul><li>Likely to be of interest to private market but beholden to market conditions and market appetite.</li></ul>
    <h4>Alternative User</h4>
    <ul><li>Limited Experience in Private Rented Sector and income led purchasers as is a relatively new market.</li></ul>
  </div>
</section>

<!-- Page 9: contact -->
<section class="page contact" style="left:771px;top:820px">
  <div class="abs column">
    <div class="brand">Harbour &amp; Meadows<small>Commercial</small></div>
    <div class="abs contact-details">
      <span class="yellow">Harbour &amp; Meadows Commercial</span><br>
      Unit 9 Carrow Road<br>London SE40 2JN<br><br>
      <span class="yellow">T:</span> 020 7946 0321<br>
      <span class="yellow">E:</span> info@harbourandmeadows.com<br>
      <span class="yellow">W:</span> www.harbourandmeadows.com
    </div>
  </div>
  <div class="abs rule"></div>
</section>

</body>
</html>
```